Homepage Header Image Redesign

We need an image redesign to be used for our Header image on the homepage. We'd like to incorporate the Rocket but it needs to look great on Desktop and mobile.

Here is the homepage: https://brightvanemedia.com/

You will notice the rocket and how it is being used. When the page scrolls, the rocket appears to be taking off. We would like to see a design that also incorporates our brand's color scheme. The concept can be the same however we would like it to be better. The image needs to fit correctly in our header.

Since we are going to have copy in middle of the screen we need to be creative with how we angle the rocketship. An idea of this is to have the ship fly diagonally from the left towards the top at a 45-degree angle. Also open to playing with rocket placement.

The current Rocket has red fins, but we would like the new rocket to have blue and/or green fins to match the color scheme of our brand.

Design ideas:
Perhaps more detailed rocket and sky with a city in the backdrop.
Perhaps more detailed rocket and sky with Downtown San Diegos city skyline in the backdrop

Open to new ideas as well. We would like to promote creative freedom!

```html
<!DOCTYPE html>
<html lang="en">
<head>
<meta charset="utf-8">
<title>Accessible and Accountable — Header</title>
<link rel="stylesheet" href="https://fonts.googleapis.com/css2?family=Oswald:wght@300;400&family=Arimo:wght@700&family=Montserrat:wght@600&display=swap">
<style>
  :root {
    --night-top: #030b1f;
    --night-mid: #0a1c44;
    --night-low: #0f2b5c;
    --water: #123a6e;
    --water-light: #1d4d86;
    --title-blue: #1f8fd2;
    --white: #ffffff;
    --cta-green: #2ea56f;
    --cta-edge: #8fdcb4;
    --art-flame: #f2a03c;
    --art-fin: #2f9f4f;
    --art-rocket: #2a7fd0;
    --art-city: #1a2b4d;
  }
  * { box-sizing: border-box; margin: 0; padding: 0; }
  html, body { width: 1200px; height: 330px; overflow: hidden; background: var(--night-top); }
  .header-banner {
    position: relative;
    width: 1200px;
    height: 330px;
    overflow: hidden;
    background: linear-gradient(180deg, var(--night-top) 0%, var(--night-mid) 55%, var(--night-low) 72%);
  }
  .waterline {
    position: absolute;
    left: 0; top: 0;
    width: 1200px; height: 330px;
  }
  .launch-illustration {
    position: absolute;
    left: 0; top: 24px;
    width: 470px; height: 306px;
    border-radius: 0 6px 0 0;
    background: linear-gradient(45deg,
      var(--art-flame) 0%,
      var(--art-fin) 24%,
      var(--art-rocket) 50%,
      var(--art-city) 82%);
  }
  .headline {
    position: absolute;
    left: 406px; top: 52px;
    font-family: "Oswald", sans-serif;
    font-weight: 300;
    font-size: 50px;
    line-height: 1;
    letter-spacing: -0.3px;
    color: var(--title-blue);
    white-space: nowrap;
    transform: scaleX(0.9);
    transform-origin: left top;
  }
  .subline {
    position: absolute;
    left: 430px; top: 129px;
    width: 340px;
    text-align: center;
    font-family: "Arimo", sans-serif;
    font-weight: 700;
    font-size: 22.5px;
    line-height: 33px;
    color: var(--white);
  }
  .cta-button {
    position: absolute;
    left: 493px; top: 224px;
    width: 231px; height: 60px;
    display: flex; align-items: center; justify-content: center;
    background: var(--cta-green);
    border: 1px solid var(--cta-edge);
    font-family: "Montserrat", sans-serif;
    font-weight: 600;
    font-size: 17px;
    letter-spacing: 5px;
    color: var(--white);
    text-decoration: none;
    padding-left: 5px;
  }
</style>
</head>
<body>
  <header class="header-banner">
    <svg class="waterline" viewBox="0 0 1200 330" aria-hidden="true">
      <rect x="0" y="237" width="1200" height="93" fill="var(--water)" opacity="0.7"/>
      <rect x="580" y="262" width="620" height="14" rx="7" fill="var(--water-light)" opacity="0.5"/>
      <rect x="600" y="290" width="600" height="8" rx="4" fill="var(--water-light)" opacity="0.45"/>
      <rect x="680" y="306" width="520" height="5" rx="2.5" fill="var(--water-light)" opacity="0.35"/>
    </svg>
    <div class="launch-illustration" role="img" aria-label="Blue rocket with green fins launching diagonally upward with an orange flame, in front of a night city skyline reflected in water"></div>
    <h1 class="headline">Accessible and Accountable</h1>
    <p class="subline">Call us today for your<br>free consultation!</p>
    <a class="cta-button" href="#contact">CONTACT US</a>
  </header>
</body>
</html>
```